WTF!!! We need a modern professional website for a business litigation law firm.

We need a modern, clean, professional and uncomplicated website for a new business trial and litigation law firm called "Hallorand Trial Firm PLLC". Website must be mobile optimized for iPad and smartphone. The law firm specializes in counseling and representing large corporations, small businesses and entrepreneurs in and out of the courtroom. Lawyers in the firm serve as Florida counsel and trial counsel to organizations facing claims involving product liability, premises liability, professional liability, vehicle and transportation liability, warranty claims, construction defects and delay claims, complex business disputes, commercial litigation and bid disputes in State and Federal Courts. The website is mainly to provide information about the firm, and should include sections describing the firm, identifying the Industries Served and Areas of Practice ," a separate page identifying the "Professionals", a separate page for "Resources & Advisories," and a traveling "Connect With Us" button a site visitor can click on that will launch an email to the Firm's general email account. The website should allow us to easily modify the content on these pages, and let us add/modify links to external information sources. We will not sell anything or take payments through the website. We do need to be able to easily upload and update photographs of attorneys and add new attorneys names/email hyperlinks as the firm grows. We would like to add developments in the law or success stories easily and quickly, such as through a blog page. On the "Connect With Us" page the website should have hyperlinks to email the Firm, and there should be hyperlinks to email each professional on the "Professionals" page. The website should be viewable on mobile devices without distortion. The law firm focuses on trial work and should have some imagery associated with courtrooms, but the overall theme of the site should be modern, clean, and communicate sophistication and strength. The website should be made in Wordpress. We have uploaded logo files for Hallorand Trial Firm.

Target Market(s)

Corporations and companies that are looking for legal representation. Other attorneys/legal industry.

Industry/Entity Type

Legal Industry

Coding

Coded - Design and coding required

Number of Pages Required

1 page

Font styles to use
Sans Serif

Requirements
Must have
• Simple, clean, sophisticated, modern website that includes the logo, watermark of logo, and the elements described above.
Nice to have
• Pictures of city scape, buildings, courtroom, team members.

```html
<!DOCTYPE html>
<html lang="en">
<head>
<meta charset="utf-8">
<title>Hallorand Trial Firm PLLC</title>
<link href="https://fonts.googleapis.com/css2?family=Poppins:ital,wght@0,400;0,500;0,600;0,700;0,800;1,400&display=swap" rel="stylesheet">
<style>
:root{
  --orange:#f26a0f;
  --ink:#111;
  --text:#555;
  --dark:#1e1e1e;
  --grey-bg:#f0f0f0;
  --line:#bdbdbd;
  --white:#fff;
}
*{margin:0;padding:0;box-sizing:border-box}
html,body{width:1200px;height:3686px;overflow:hidden}
body{font-family:'Poppins',sans-serif;color:var(--ink);background:var(--white);position:relative}
.abs{position:absolute}
.btn{position:absolute;background:var(--orange);color:var(--white);font-weight:600;display:flex;align-items:center;justify-content:center;font-size:17px}

/* header */
.topbar{top:0;left:0;width:1200px;height:110px;background:var(--white)}
.brand{left:74px;top:18px;text-align:center;width:140px}
.brand-mark{width:40px;height:40px;background:var(--ink);margin:0 auto 4px}
.brand-name{font-weight:800;font-size:23px;letter-spacing:0;line-height:1}
.brand-sub{font-weight:600;font-size:10px;letter-spacing:3px}
.call-icon{left:585px;top:29px;width:50px;height:50px;border-radius:50%;background:var(--ink)}
.call-label{left:643px;top:28px;font-weight:600;font-size:17px}
.call-num{left:643px;top:48px;font-weight:700;font-size:27px}
.top-btn{left:904px;top:30px;width:222px;height:52px;font-size:19px}
.nav{top:110px;left:0;width:1200px;height:50px;background:var(--dark);display:flex;align-items:center;padding-left:117px;gap:44px}
.nav span{color:var(--white);font-weight:600;font-size:14px}
.nav .active{color:var(--orange);text-decoration:underline;text-underline-offset:5px}

/* hero */
.hero{top:160px;left:0;width:1200px;height:610px;background:linear-gradient(180deg,#6e6158 0%,#8a7565 45%,#5a4638 100%)}
.hero-shade{inset:0;background:rgba(0,0,0,.25)}
.hero-title{top:132px;left:0;width:1200px;text-align:center;color:var(--white);font-weight:800;font-size:102px;line-height:1;letter-spacing:2px}
.hero-title2{top:230px;left:0;width:1200px;text-align:center;color:var(--white);font-weight:600;font-size:94px;line-height:1;letter-spacing:3px}
.hero-sub{top:320px;left:0;width:1200px;text-align:center;color:var(--white);font-weight:500;font-size:27px;line-height:34px}
.hero-btn{left:485px;top:405px;width:230px;height:51px}
.dots{display:flex;gap:11px}
.dots i{width:11px;height:11px;background:#bbb;display:block}
.dots i.on{background:#222}

/* about */
.about-block{left:0;top:844px;width:343px;height:446px;background:linear-gradient(135deg,#3d3d3d,#2a2a2a)}
.about-photo{left:164px;top:885px;width:422px;height:365px;background:linear-gradient(135deg,#8a8f96,#c9c8c4 50%,#3a3e45)}
h2{font-weight:500;font-size:50px;line-height:54px;color:var(--ink)}
h2 b{font-weight:800}
.about-h{left:618px;top:874px}
.para{font-size:15px;line-height:28px;color:var(--text)}
.about-p{left:616px;top:1000px;width:510px}
.about-btn{left:616px;top:1198px;width:163px;height:52px}

/* practice */
.practice{left:0;top:1359px;width:1200px;height:658px;background:var(--grey-bg)}
.practice-h{left:74px;top:62px}
.practice-p{left:73px;top:175px;width:340px;font-size:14px;line-height:24px;color:var(--text)}
.practice-btn{left:74px;top:268px;width:195px;height:53px}
.card{position:absolute;width:332px;height:267px;background:var(--white);border:1px solid var(--line);padding:18px 15px}
.card svg{width:76px;height:76px;display:block;stroke:var(--ink);fill:none;stroke-width:2.4}
.card h3{font-weight:700;font-size:24px;line-height:28px;margin:14px 0 10px}
.card p{font-size:13px;line-height:21px;color:var(--text)}
.card a{display:inline-block;margin-top:10px;color:var(--orange);font-size:14px;font-weight:500;text-decoration:underline}
.card.dark{background:var(--dark);border-color:var(--dark)}
.card.dark svg{stroke:var(--white)}
.card.dark h3{color:var(--white)}
.card.dark p{color:#ccc}

/* team */
.team{left:0;top:2058px;width:1200px;height:452px;background:linear-gradient(90deg,#e0e0e0,#eeeeee)}
.team-photo{left:0;top:0;width:586px;height:452px;background:linear-gradient(135deg,#6d7a8a,#b8b4ad 50%,#525a66)}
.team-h{left:614px;top:62px}
.team-p{left:612px;top:168px;width:520px}
.team-btn{left:613px;top:337px;width:181px;height:52px}

/* industries */
.ind-h{left:0;top:2560px;width:1200px;text-align:center}
.clients{left:74px;top:2648px;width:1052px;display:flex;justify-content:space-between;align-items:center}
.clients span{font-size:34px;font-weight:600;color:#7a7a7a}

/* stories */
.stories{left:0;top:2810px;width:1200px;height:418px;background:linear-gradient(135deg,#2c2c2c,#151515 60%,#242424)}
.client-photo{left:166px;top:104px;width:206px;height:206px;border-radius:50%;background:linear-gradient(135deg,#d6dbe2,#8aa0bf 60%,#3f5f8f)}
.stories h2{color:var(--white)}
.story-h{left:400px;top:78px}
.quote{left:402px;top:156px;width:600px;color:var(--white);font-style:italic;font-size:15px;line-height:28px}
.quote-by{left:402px;top:305px;color:var(--orange);font-weight:700;font-size:18px}

/* footer */
.foot-h{font-weight:700;font-size:21px}
.foot-list{font-size:13px;line-height:34px;color:#222;list-style:none}
.ico{position:absolute;width:45px;height:45px;border-radius:50%;background:var(--ink)}
.ico svg{width:45px;height:45px}
.foot-txt{position:absolute;font-size:13px;line-height:22px;color:#222}
.social{left:74px;top:3539px;display:flex;gap:20px}
.social i{width:22px;height:22px;background:#333;display:block;border-radius:3px}
.social i.on{background:var(--orange)}
.copy{left:0;top:3618px;width:1200px;height:68px;border-top:1px solid #ddd;text-align:center;font-size:12px;color:#444;padding-top:28px}
</style>
</head>
<body>

<header class="abs topbar">
  <div class="abs brand">
    <div class="brand-mark"></div>
    <div class="brand-name">HALLORAND</div>
    <div class="brand-sub">TRIAL FIRM</div>
  </div>
  <div class="abs call-icon">
    <svg viewBox="0 0 50 50" width="50" height="50"><path d="M19 15c-2 1-3 3-2 6 2 6 6 11 12 14 3 1 5 0 6-2l-4-4-3 2c-3-2-5-4-7-7l2-3z" fill="#fff"/></svg>
  </div>
  <div class="abs call-label">CALL US</div>
  <div class="abs call-num">+1-555-014-2290</div>
  <div class="btn top-btn">CONNECT WITH US</div>
</header>

<nav class="abs nav">
  <span class="active">HOME</span><span>ABOUT US</span><span>PRACTICE AREAS</span><span>PROFESSIONALS</span><span>RESOURCES &amp; ADVISORIES</span><span>BLOG</span><span>CONTACT US</span>
</nav>

<section class="abs hero" role="img" aria-label="Law office interior with city view through tall windows">
  <div class="abs hero-shade"></div>
  <div class="abs hero-title">HALLORAND</div>
  <div class="abs hero-title2">TRIAL FIRM</div>
  <div class="abs hero-sub">Sed ut perspiciatis unde omnis iste natus error sit volup<br>tatem accusantium.</div>
  <div class="btn hero-btn">CONNECT WITH US</div>
  <div class="abs dots" style="left:563px;top:550px"><i class="on"></i><i></i><i></i><i></i></div>
</section>

<section>
  <div class="abs about-block"></div>
  <div class="abs about-photo" role="img" aria-label="Three attorneys reviewing documents together"></div>
  <h2 class="abs about-h"><b>About Hallorand</b><br>Trial Firm PLLC</h2>
  <p class="abs para about-p">Sed ut perspiciatis unde omnis iste natus error sit voluptatem accusantium doloremque laudantium, totam rem aperiam, eaque ipsa quae ab illo inventore veritatis et quasi architecto beatae vitae dicta sunt explicabo. Nemo enim ipsam voluptatem quia voluptas sit aspernatur aut odit aut fugit, sed quia consequuntur magni dolores eos qui ratione voluptatem.</p>
  <div class="btn about-btn">Read More</div>
</section>

<section class="abs practice">
  <h2 class="abs practice-h"><b>Areas</b><br><b>of</b> Practice</h2>
  <p class="abs practice-p">Sed ut perspiciatis unde omnis iste natus error sit voluptatemaccusantium doloremque laudantium, totam rem aperiam.</p>
  <div class="btn practice-btn">View All Practice</div>

  <div class="card" style="left:433px;top:63px">
    <svg viewBox="0 0 76 76"><circle cx="32" cy="20" r="11"/><path d="M12 64V52c0-9 8-14 20-14s20 5 20 14v12z"/><circle cx="56" cy="52" r="10"/><path d="M51 52l4 4 7-8"/></svg>
    <h3>Professional Liability</h3>
    <p>Sed ut perspiciatis unde omnis iste natus error sit voluptatemaccusa ntiumloemque laudantium, totam rem aperiam.</p>
    <a>Learn More</a>
  </div>
  <div class="card dark" style="left:794px;top:63px">
    <svg viewBox="0 0 76 76"><rect x="28" y="12" width="32" height="54"/><path d="M34 20h6M46 20h6M34 30h6M46 30h6M34 40h6M46 40h6M34 50h6M46 50h6"/><circle cx="16" cy="40" r="9"/><path d="M16 49v17"/></svg>
    <h3>Premises Liability</h3>
    <p>Sed ut perspiciatis unde omnis iste natus error sit voluptatemaccusa ntiumloemque laudantium, totam rem aperiam.</p>
    <a>Learn More</a>
  </div>
  <div class="card" style="left:70px;top:356px">
    <svg viewBox="0 0 76 76"><rect x="16" y="10" width="44" height="58"/><path d="M30 20l8-3 8 3v8c0 5-4 8-8 10-4-2-8-5-8-10z"/><path d="M24 48h28M24 56h28"/></svg>
    <h3>Product Liability</h3>
    <p>Sed ut perspiciatis unde omnis iste natus error sit voluptatemaccusa ntiumloemque laudantium, totam rem aperiam.</p>
    <a>Learn More</a>
  </div>
  <div class="card" style="left:433px;top:356px">
    <svg viewBox="0 0 76 76"><rect x="10" y="10" width="40" height="52"/><path d="M17 20h26M17 28h26M17 36h20M17 44h16"/><path d="M56 40l12 4v10c0 7-6 11-12 14-6-3-12-7-12-14V44z"/><path d="M51 54l4 4 7-8"/></svg>
    <h3>Warranty Claims</h3>
    <p>Sed ut perspiciatis unde omnis iste natus error sit voluptatemaccusa ntiumloemque laudantium, totam rem aperiam.</p>
    <a>Learn More</a>
  </div>
  <div class="card" style="left:794px;top:356px">
    <svg viewBox="0 0 76 76"><rect x="36" y="8" width="30" height="44"/><path d="M42 18h18M42 26h18M42 34h12"/><path d="M8 58V44l6-10h18v24z"/><circle cx="16" cy="60" r="5"/><path d="M14 40h14"/></svg>
    <h3>Vehicle and Transportation Liability</h3>
    <p>Sed ut perspiciatis unde omnis iste natus error sit voluptatemaccusa ntiumloemque laudantium, totam rem aperiam.</p>
    <a>Learn More</a>
  </div>
</section>

<section class="abs team">
  <div class="abs team-photo" role="img" aria-label="Group portrait of the firm's attorneys"></div>
  <h2 class="abs team-h"><b>Meet The</b><br>Team</h2>
  <p class="abs para team-p">Sed ut perspiciatis unde omnis iste natus error sit voluptatem accusantium doloremque laudantium, totam rem aperiam, eaque ipsa quae ab illo inventore veritatis et quasi architecto beatae vitae dicta sunt explicabo. Nemo enim ipsam voluptatem quia voluptas sit aspernatur aut odit aut fugit.</p>
  <div class="btn team-btn">Meet Our Team</div>
</section>

<section>
  <h2 class="abs ind-h"><b>Industries</b> Served</h2>
  <div class="abs clients"><span>Brightmere</span><span>Corvane Group</span><span>Talvero</span><span>Lindqvist &amp; Rowe</span></div>
  <div class="abs dots" style="left:573px;top:2730px"><i class="on" style="border-radius:50%;width:9px;height:9px"></i><i style="border-radius:50%;width:9px;height:9px"></i><i style="border-radius:50%;width:9px;height:9px"></i><i style="border-radius:50%;width:9px;height:9px"></i></div>
</section>

<section class="abs stories" role="img" aria-label="Dark background of a business handshake">
  <svg class="abs" style="left:112px;top:190px" width="28" height="40" viewBox="0 0 28 40"><path d="M22 4L6 20l16 16" stroke="#fff" stroke-width="3" fill="none"/></svg>
  <svg class="abs" style="left:1060px;top:190px" width="28" height="40" viewBox="0 0 28 40"><path d="M6 4l16 16L6 36" stroke="#f26a0f" stroke-width="3" fill="none"/></svg>
  <div class="abs client-photo" role="img" aria-label="Portrait of a satisfied client"></div>
  <h2 class="abs story-h"><b>Success</b> Stories</h2>
  <p class="abs quote">“ Sed ut perspiciatis unde omnis iste natus error sit voluptatem accusantium doloremque laudantium, totam rem aperiam, eaque ipsa quae ab illo inventore veritatis et quasi architecto beatae vitae dicta sunt explicaboemo enim ipsam voluptatem quia voluptas sit aspernatur aut odit aut fugit, sed quia consequuntur magni dolores eos qui ratione voluptatem..”</p>
  <div class="abs quote-by">- Name Heading</div>
</section>

<footer>
  <div class="abs foot-h" style="left:74px;top:3290px">Contact Address</div>
  <div class="ico" style="left:74px;top:3340px"><svg viewBox="0 0 45 45"><path d="M22.5 13a6 6 0 0 0-6 6c0 5 6 12 6 12s6-7 6-12a6 6 0 0 0-6-6z" fill="#fff"/><circle cx="22.5" cy="19" r="2" fill="#111"/></svg></div>
  <div class="foot-txt" style="left:135px;top:3340px">48 Harbor Lane Suite 210,<br>Tampa FL 33602, United States</div>
  <div class="ico" style="left:74px;top:3398px"><svg viewBox="0 0 45 45"><path d="M17 14c-2 1-2 3-2 5 2 5 5 9 10 11 2 1 4 0 5-2l-3-3-2 1c-2-1-4-3-5-5l1-2z" fill="#fff"/></svg></div>
  <div class="foot-txt" style="left:135px;top:3410px;font-size:14px">+1 555 014 2290</div>
  <div class="ico" style="left:74px;top:3453px"><svg viewBox="0 0 45 45"><rect x="14" y="16" width="17" height="13" fill="#fff"/><path d="M14 16l8.5 7 8.5-7" stroke="#111" stroke-width="1.5" fill="none"/></svg></div>
  <div class="foot-txt" style="left:135px;top:3465px;font-size:14px">info@hallorandfirm.com</div>
  <div class="abs social"><i></i><i class="on"></i><i></i><i></i><i></i></div>

  <div class="abs foot-h" style="left:395px;top:3292px">Quick Links</div>
  <ul class="abs foot-list" style="left:395px;top:3325px"><li>Home</li><li>About Us</li><li>Practice Areas</li><li>Professionals</li><li>Resources &amp; Advisories</li><li>Blog</li><li>Contact Us</li></ul>

  <div class="abs foot-h" style="left:629px;top:3292px">Areas of Practice</div>
  <ul class="abs foot-list" style="left:629px;top:3325px"><li>Product Liability</li><li>Premises Liability</li><li>Professional Liability</li><li>Vehicle &amp; Transportation Liability</li><li>Warranty Claims</li></ul>
  <ul class="abs foot-list" style="left:884px;top:3325px"><li>Construction Defects &amp; Delay Claims</li><li>Complex Business Disputes</li><li>Commercial Litigation</li><li>Bid Disputes</li></ul>

  <div class="abs copy">Copyright © 2024.Company Name. All Right Reserved</div>
</footer>

</body>
</html>
```